Our Company name is Bluefield Office Cleaning Services. We are a Toronto(GTA) company looking for a brochure that with Logo design that gives a description of what we do.

We are a company that specializes in cleaning and sanitizing office/ workplaces. Our Experience includes working with school boards and hospitals, and have 15 plus years experience. We are looking for a simple design that catches and explains to our customers what we offer with some pics, which you can provide.

if you have any questions please let us know.

thank you

Target Market(s)

We are focusing Businesses

Font styles to use
Serif

Colors

Designer to choose colors to be used in the design.

Requirements
Must have
• Must have our name/Logo, brief description of what we do. Contact numbers, (416)-555-0183/ (647)555-0927 email (bluefieldofficecleaningservices@mailbox-example.com
• Pics which you can provide
Nice to have
• We trust your imagination on this

```html
<!DOCTYPE html>
<html lang="en">
<head>
<meta charset="utf-8">
<title>Bluefield Office Cleaning Services – Trifold Brochure</title>
<link href="https://fonts.googleapis.com/css2?family=Open+Sans:wght@400;600;700;800&display=swap" rel="stylesheet">
<style>
  :root{
    --navy:#173a86;
    --blue:#1f5cb0;
    --sky:#1b8ac9;
    --deep:#123172;
    --green:#8cc63f;
    --green-dark:#6fa82a;
    --gold:#c9a227;
    --gold-light:#ecd27a;
    --paper:#ffffff;
    --ink:#33415c;
    --stage:#e4e4e4;
    --photo-a:#c9ced6;
    --photo-b:#8e98a8;
  }
  *{box-sizing:border-box;margin:0;padding:0}
  html,body{width:1200px;height:2400px;overflow:hidden}
  body{background:var(--stage);font-family:"Open Sans",Arial,sans-serif;color:var(--ink);position:relative}

  .spread{position:absolute;left:50px;width:1100px;height:850px;display:grid;grid-template-columns:repeat(3,1fr);box-shadow:0 18px 40px rgba(0,0,0,.18);background:var(--paper)}
  .spread--outside{top:230px}
  .spread--inside{top:1320px}
  .panel{position:relative;overflow:hidden}

  .photo{position:absolute;background:linear-gradient(160deg,var(--photo-a),var(--photo-b))}
  .wave{position:absolute;left:0;width:100%}

  /* wordmark */
  .wordmark{text-align:center;color:var(--navy);font-weight:800;line-height:1}
  .wordmark__name{display:block;font-size:40px;letter-spacing:2px}
  .wordmark__sub{display:block;font-size:12.5px;letter-spacing:1px;margin-top:6px}

  .pill{display:flex;align-items:center;justify-content:center;gap:10px;border-radius:30px;font-weight:700;color:#fff}
  .pill--navy{background:var(--navy)}
  .pill--green{background:var(--green)}
  .pill svg{width:22px;height:22px}

  .seal{position:absolute;border-radius:50%;background:radial-gradient(circle at 40% 35%,var(--gold-light),var(--gold) 60%,#8d6e12);border:4px solid #fff;box-shadow:0 3px 8px rgba(0,0,0,.3)}

  /* cover */
  .cover__logo{position:absolute;top:58px;left:0;width:100%}
  .cover__photo{top:160px;left:0;width:100%;height:420px}
  .cover__tagline{position:absolute;top:628px;width:100%;text-align:center;color:var(--green-dark);font-weight:800;font-size:21px;letter-spacing:.5px}
  .cover__phone{position:absolute;top:680px;left:40px;right:40px;height:52px;font-size:24px}
  .cover__email{position:absolute;top:752px;width:100%;text-align:center;font-size:11.5px;color:var(--navy);font-weight:600}

  /* contact panel */
  .contact{background:linear-gradient(180deg,var(--blue),var(--deep))}
  .contact__circle{top:40px;left:98px;width:170px;height:170px;border-radius:50%;border:6px solid #fff}
  .contact__title{position:absolute;top:232px;width:100%;text-align:center;color:#fff;font-size:19px;font-weight:800;letter-spacing:1px}
  .contact__text{position:absolute;left:34px;right:34px;color:#fff;font-size:12.5px;line-height:1.6;text-align:center}
  .contact__text--top{top:268px}
  .contact__text--bottom{top:560px;text-align:left}
  .contact__phones{position:absolute;top:388px;left:28px;right:28px;height:40px;font-size:14px}
  .contact__social{position:absolute;top:448px;width:100%;display:flex;justify-content:center;gap:12px}
  .contact__social span{width:24px;height:24px;border-radius:50%;background:#fff;opacity:.9}
  .contact__email{position:absolute;top:494px;width:100%;text-align:center;color:#fff;font-size:11px;font-weight:700}

  /* services panel */
  .services__photo{top:0;left:0;width:100%;height:270px}
  .services__tab{position:absolute;top:292px;left:0;width:78%;height:34px;background:var(--navy);color:#fff;font-weight:700;font-size:13px;letter-spacing:.5px;display:flex;align-items:center;padding-left:40px;border-radius:0 20px 20px 0}
  .services__list{position:absolute;top:350px;left:34px;right:24px;list-style:none}
  .services__list li{display:flex;gap:14px;align-items:center;margin-bottom:22px}
  .services__icon{flex:none;width:42px;height:42px;border-radius:50%;background:var(--green);display:flex;align-items:center;justify-content:center}
  .services__icon svg{width:20px;height:20px}
  .services__name{display:block;color:var(--navy);font-weight:800;font-size:13px;letter-spacing:.5px}
  .services__desc{display:block;font-size:11.5px;color:#5b6478}

  /* inside left */
  .impression{background:var(--paper)}
  .impression__photo{top:0;left:0;width:100%;height:380px}
  .impression__body{position:absolute;top:360px;left:0;width:100%;height:490px;background:linear-gradient(180deg,var(--sky),var(--blue));padding:58px 30px 0}
  .impression__title{color:var(--green);font-size:17px;font-weight:800;line-height:1.3;margin-bottom:16px}
  .impression__text{color:#fff;font-size:11.8px;line-height:1.6;margin-bottom:12px}

  /* inside middle */
  .plan__logo{position:absolute;top:42px;width:100%}
  .plan__logo .wordmark__name{font-size:32px}
  .plan__logo .wordmark__sub{font-size:10.5px}
  .plan__intro{position:absolute;top:136px;left:30px;right:30px;font-size:12px;line-height:1.6;text-align:center}
  .plan__list{position:absolute;top:236px;left:36px;right:24px;list-style:none}
  .plan__list li{font-size:12.5px;line-height:1.3;margin-bottom:9px;padding-left:20px;position:relative}
  .plan__list li::before{content:"";position:absolute;left:0;top:4px;width:9px;height:9px;background:var(--green);transform:rotate(45deg)}
  .plan__photo{top:622px;left:30px;right:30px;height:130px;border-radius:14px;background:linear-gradient(135deg,#dfe9f4,#9fb8d6 55%,#c5a7c9)}
  .plan__phone{position:absolute;top:772px;left:40px;right:40px;height:42px;font-size:19px}

  /* inside right */
  .why__top{position:absolute;top:0;left:0;width:100%;height:560px;background:linear-gradient(180deg,var(--sky),var(--blue))}
  .why__title{position:absolute;top:36px;left:32px;color:#fff;font-size:18px;font-weight:800;letter-spacing:.5px}
  .why__list{position:absolute;top:80px;left:30px;right:24px;list-style:none}
  .why__list li{display:flex;gap:10px;align-items:flex-start;color:#fff;font-size:12.5px;line-height:1.35;margin-bottom:13px}
  .why__list svg{flex:none;width:17px;height:17px;margin-top:1px}
  .why__photo{top:540px;left:0;width:100%;height:310px}
</style>
</head>
<body>

<!-- Outside spread -->
<section class="spread spread--outside">

  <article class="panel services">
    <div class="photo services__photo" role="img" aria-label="Photo of a cleaner mopping a bright office floor by large windows"></div>
    <svg class="wave" style="top:230px;height:60px" viewBox="0 0 366 60" preserveAspectRatio="none" aria-hidden="true">
      <path d="M0 30 Q180 0 366 20 L366 60 L0 60Z" fill="var(--green)"/>
      <path d="M0 40 Q180 12 366 32 L366 60 L0 60Z" fill="#fff"/>
    </svg>
    <div class="services__tab">OUR CLEANING SERVICES</div>
    <ul class="services__list">
      <li><span class="services__icon"><svg viewBox="0 0 20 20"><rect x="4" y="3" width="12" height="15" fill="#fff"/></svg></span><span><span class="services__name">COMMERCIAL</span><span class="services__desc">Offices, retail and lobbies</span></span></li>
      <li><span class="services__icon"><svg viewBox="0 0 20 20"><path d="M10 2 L17 5 V10 C17 14 10 18 10 18 C10 18 3 14 3 10 V5Z" fill="#fff"/></svg></span><span><span class="services__name">SAFETY</span><span class="services__desc">Sanitizing high-touch surfaces</span></span></li>
      <li><span class="services__icon"><svg viewBox="0 0 20 20"><path d="M8 3h4v5h5v4h-5v5H8v-5H3V8h5z" fill="#fff"/></svg></span><span><span class="services__name">HEALTHCARE</span><span class="services__desc">Clinics and hospital wards</span></span></li>
      <li><span class="services__icon"><svg viewBox="0 0 20 20"><path d="M10 3 L19 8 L10 13 L1 8Z M5 11v4c3 2 7 2 10 0v-4" fill="#fff"/></svg></span><span><span class="services__name">EDUCATIONAL</span><span class="services__desc">Schools, colleges and campuses</span></span></li>
      <li><span class="services__icon"><svg viewBox="0 0 20 20"><path d="M2 18V9l5 3V9l5 3V4h6v14Z" fill="#fff"/></svg></span><span><span class="services__name">INDUSTRIAL</span><span class="services__desc">Warehouses and plant floors</span></span></li>
    </ul>
  </article>

  <article class="panel contact">
    <svg class="wave" style="top:0;height:130px" viewBox="0 0 366 130" preserveAspectRatio="none" aria-hidden="true">
      <path d="M0 0 H366 V60 Q180 130 0 90Z" fill="#fff"/>
      <path d="M0 90 Q180 130 366 60 V70 Q180 142 0 100Z" fill="var(--green)"/>
    </svg>
    <div class="photo contact__circle" role="img" aria-label="Photo of a cleaner mopping an office corridor"></div>
    <h2 class="contact__title">CONTACT US</h2>
    <p class="contact__text contact__text--top">We are a company that specializes in cleaning and sanitizing office/ workplaces. Our experience includes working with school boards and hospitals, and we have 15 plus years experience.</p>
    <div class="pill pill--green contact__phones">(416)-555-0183 &nbsp;|&nbsp; (647)555-0927</div>
    <div class="contact__social" aria-hidden="true"><span></span><span></span><span></span><span></span></div>
    <p class="contact__email">bluefieldofficecleaningservices@mailbox-example.com</p>
    <p class="contact__text contact__text--bottom">Bluefield Cleaning Services makes it easy to reach us when you need help with your business. Our customer service agents are waiting for you. Simply use the form below or contact us toll-free at (647)555-0927 to learn more about our services and products.</p>
  </article>

  <article class="panel cover">
    <svg class="wave" style="top:0;height:170px" viewBox="0 0 366 170" preserveAspectRatio="none" aria-hidden="true">
      <path d="M0 140 Q200 175 366 120 V150 Q200 200 0 165Z" fill="var(--green)"/>
      <path d="M0 150 Q200 188 366 134 V170 H0Z" fill="var(--navy)"/>
    </svg>
    <div class="cover__logo wordmark"><span class="wordmark__name">BLUEFIELD</span><span class="wordmark__sub">OFFICE CLEANING SERVICES</span></div>
    <div class="photo cover__photo" role="img" aria-label="Photo of a smiling cleaner in a blue apron with a mop in a modern office"></div>
    <svg class="wave" style="top:540px;height:60px" viewBox="0 0 366 60" preserveAspectRatio="none" aria-hidden="true">
      <path d="M0 40 Q200 0 366 10 V60 H0Z" fill="var(--green)"/>
      <path d="M0 50 Q200 14 366 24 V60 H0Z" fill="#fff"/>
    </svg>
    <div class="seal" style="top:470px;left:24px;width:96px;height:96px"></div>
    <p class="cover__tagline">CLEANING SERVICES THAT SHINE</p>
    <div class="pill pill--navy cover__phone"><svg viewBox="0 0 24 24"><circle cx="12" cy="12" r="11" fill="#fff"/><path d="M8 6l2 3-1 1.5c.8 1.8 2.2 3.2 4 4L14.5 13l3 2-1 2.5C12 17 7 12 6.5 7.5Z" fill="var(--navy)"/></svg>(647)555-0927</div>
    <p class="cover__email">bluefieldofficecleaningservices@mailbox-example.com</p>
  </article>
</section>

<!-- Inside spread -->
<section class="spread spread--inside">

  <article class="panel impression">
    <div class="photo impression__photo" role="img" aria-label="Photo of a cleaner wiping a boardroom table"></div>
    <svg class="wave" style="top:320px;height:70px;z-index:2" viewBox="0 0 366 70" preserveAspectRatio="none" aria-hidden="true">
      <path d="M0 30 Q180 0 366 40 V70 H0Z" fill="var(--green)"/>
      <path d="M0 42 Q180 12 366 52 V70 H0Z" fill="var(--sky)"/>
    </svg>
    <div class="impression__body">
      <h2 class="impression__title">MAKE YOUR CORPORATE IMPRESSION STRONG WITH THE RIGHT OFFICE CLEANING SERVICES</h2>
      <p class="impression__text">Having a clean and well-maintained office premise is paramount if you want to lead in your business industry. For this, most business owners appoint janitors, who perform all the cleaning tasks of their offices. But it can be an extra burden for your business.</p>
      <p class="impression__text">Therefore, if you are looking for a budget friendly cleaning solution for your office, you can hire professional office cleaning services in Toronto/GTA to maintain the cleanliness in your office.</p>
      <p class="impression__text">When your office is clean and well-kept, your employees also enjoy their work and in this way your business efficiency will boost.</p>
    </div>
  </article>

  <article class="panel plan">
    <div class="plan__logo wordmark"><span class="wordmark__name">BLUEFIELD</span><span class="wordmark__sub">OFFICE CLEANING SERVICES</span></div>
    <p class="plan__intro">We will work hard to craft a plan that meets your needs without breaking your budget. Though the needs of each customer are different, the basic cleaning service includes the following:</p>
    <ul class="plan__list">
      <li>Daily, weekly, monthly cleaning services</li>
      <li>Dusting</li>
      <li>Vacuuming</li>
      <li>Trash Removal</li>
      <li>Breakroom Cleanup</li>
      <li>Bathroom cleaning and disinfecting</li>
      <li>Sweeping and mopping of hard surface floors</li>
      <li>Complete Floor Care Programs</li>
      <li>Cleaning For Special Events</li>
      <li>Window Cleaning</li>
    </ul>
    <div class="photo plan__photo" role="img" aria-label="Photo of cleaning supplies, gloves and a vacuum"></div>
    <div class="pill pill--navy plan__phone"><svg viewBox="0 0 24 24"><circle cx="12" cy="12" r="11" fill="#fff"/><path d="M8 6l2 3-1 1.5c.8 1.8 2.2 3.2 4 4L14.5 13l3 2-1 2.5C12 17 7 12 6.5 7.5Z" fill="var(--navy)"/></svg>(647)555-0927</div>
  </article>

  <article class="panel why">
    <div class="why__top"></div>
    <h2 class="why__title">WHY CHOOSE US?</h2>
    <ul class="why__list">
      <li><svg viewBox="0 0 18 18"><circle cx="9" cy="9" r="8" fill="none" stroke="#fff" stroke-width="1.6"/><path d="M5 9l3 3 5-6" fill="none" stroke="#fff" stroke-width="2"/></svg>Always have a personal point of contact.</li>
      <li><svg viewBox="0 0 18 18"><circle cx="9" cy="9" r="8" fill="none" stroke="#fff" stroke-width="1.6"/><path d="M5 9l3 3 5-6" fill="none" stroke="#fff" stroke-width="2"/></svg>Full-service cleaning management.</li>
      <li><svg viewBox="0 0 18 18"><circle cx="9" cy="9" r="8" fill="none" stroke="#fff" stroke-width="1.6"/><path d="M5 9l3 3 5-6" fill="none" stroke="#fff" stroke-width="2"/></svg>Bespoke service suited to your requirements.</li>
      <li><svg viewBox="0 0 18 18"><circle cx="9" cy="9" r="8" fill="none" stroke="#fff" stroke-width="1.6"/><path d="M5 9l3 3 5-6" fill="none" stroke="#fff" stroke-width="2"/></svg>Ethical employees.</li>
      <li><svg viewBox="0 0 18 18"><circle cx="9" cy="9" r="8" fill="none" stroke="#fff" stroke-width="1.6"/><path d="M5 9l3 3 5-6" fill="none" stroke="#fff" stroke-width="2"/></svg>Over 15+ years of satisfied customers.</li>
      <li><svg viewBox="0 0 18 18"><circle cx="9" cy="9" r="8" fill="none" stroke="#fff" stroke-width="1.6"/><path d="M5 9l3 3 5-6" fill="none" stroke="#fff" stroke-width="2"/></svg>Free No Obligation Quote.</li>
      <li><svg viewBox="0 0 18 18"><circle cx="9" cy="9" r="8" fill="none" stroke="#fff" stroke-width="1.6"/><path d="M5 9l3 3 5-6" fill="none" stroke="#fff" stroke-width="2"/></svg>Security Of A Fully Bonded Company.</li>
      <li><svg viewBox="0 0 18 18"><circle cx="9" cy="9" r="8" fill="none" stroke="#fff" stroke-width="1.6"/><path d="M5 9l3 3 5-6" fill="none" stroke="#fff" stroke-width="2"/></svg>100% Satisfaction Guarantee On All Services.</li>
      <li><svg viewBox="0 0 18 18"><circle cx="9" cy="9" r="8" fill="none" stroke="#fff" stroke-width="1.6"/><path d="M5 9l3 3 5-6" fill="none" stroke="#fff" stroke-width="2"/></svg>A Fully Insured Company.</li>
    </ul>
    <div class="photo why__photo" role="img" aria-label="Photo of a floor scrubbing machine cleaning a shiny office floor"></div>
    <svg class="wave" style="top:500px;height:70px" viewBox="0 0 366 70" preserveAspectRatio="none" aria-hidden="true">
      <path d="M0 0 H366 V30 Q180 70 0 40Z" fill="var(--blue)"/>
      <path d="M0 40 Q180 70 366 30 V40 Q180 82 0 52Z" fill="var(--green)"/>
    </svg>
    <div class="seal" style="top:470px;left:246px;width:90px;height:90px"></div>
  </article>
</section>

</body>
</html>
```